Sales Process

I need a card/page to hand out to my new clients that gives them an over view of our sales process start to finish. Along with 3 points that set us apart from all other competition.
The attached file is my first attempt with other ideas so give your suggestions.
Check out my website to get an idea of who we are. www.brindlefernyards.com

```html
<!DOCTYPE html>
<html lang="en">
<head>
<meta charset="utf-8">
<title>Brindle Fern Yards – Our Process</title>
<link rel="stylesheet" href="https://fonts.googleapis.com/css2?family=Cinzel:wght@600;700&family=Montserrat:wght@600;700;800;900&family=Open+Sans:ital@1&display=swap">
<style>
  :root {
    --green: #8cc63f;
    --green-light: #b9de8a;
    --green-dark: #66a233;
    --ink: #4d4d4f;
    --road: #555557;
    --paper: #ffffff;
  }
  * { margin: 0; padding: 0; box-sizing: border-box; }
  html, body { width: 1200px; height: 848px; overflow: hidden; background: var(--paper); }
  .sheet { position: relative; width: 1200px; height: 848px; background: var(--paper); color: var(--ink); }
  .route { position: absolute; inset: 0; width: 1200px; height: 848px; }

  .headline { position: absolute; left: 58px; top: 66px; display: flex; align-items: flex-start; }
  .headline-number {
    font-family: "Montserrat", sans-serif; font-weight: 900; color: var(--green);
    font-size: 188px; line-height: 0.8; letter-spacing: -6px; margin-top: 4px;
  }
  .headline-text {
    font-family: "Cinzel", serif; font-weight: 700; font-size: 45px; line-height: 46px;
    color: var(--ink); margin-left: 6px; margin-top: 6px;
  }
  .advantages { position: absolute; left: 68px; top: 243px; list-style: none;
    font-family: "Cinzel", serif; font-weight: 700; font-size: 18px; color: var(--ink); }
  .advantages li { height: 35px; }

  .step { position: absolute; font-family: "Montserrat", sans-serif; color: var(--ink); }
  .step-title { font-weight: 800; font-size: 25px; line-height: 31px; }
  .step-note { font-weight: 600; font-size: 14.5px; line-height: 21px; margin-top: 4px; }
  .step--right { text-align: right; }
  .step-call { right: 994px; top: 610px; }
  .step-visit { left: 554px; top: 576px; }
  .step-design { right: 656px; top: 385px; }
  .step-install { left: 894px; top: 364px; }
  .step-complete { right: 302px; top: 164px; }

  .brand { position: absolute; left: 812px; top: 668px; display: flex; align-items: center; gap: 12px; }
  .brand-dot { width: 34px; height: 34px; border-radius: 50%; background: var(--green); }
  .brand-name { font-family: "Montserrat", sans-serif; font-weight: 800; font-size: 33px; color: var(--ink); letter-spacing: 1px; }
  .tagline { position: absolute; left: 833px; top: 779px;
    font-family: "Open Sans", sans-serif; font-style: italic; font-size: 14.5px; color: var(--ink); }
</style>
</head>
<body>
<main class="sheet">
  <svg class="route" viewBox="0 0 1500 1060" aria-hidden="true">
    <defs>
      <linearGradient id="badge-fill" x1="0" y1="0" x2="1" y2="1">
        <stop offset="0" stop-color="#c4e49b"/>
        <stop offset="1" stop-color="#5e9d2f"/>
      </linearGradient>
    </defs>
    <g class="road" fill="none">
      <path d="M0 938 H340 C430 938 470 880 470 800 V740 C470 670 520 632 600 632 H770 C850 632 890 580 895 520 L900 460 C905 400 950 370 1010 370 H1220 C1300 370 1350 320 1350 240 V0"
            stroke="var(--road)" stroke-width="30"/>
      <path d="M0 938 H340 C430 938 470 880 470 800 V740 C470 670 520 632 600 632 H770 C850 632 890 580 895 520 L900 460 C905 400 950 370 1010 370 H1220 C1300 370 1350 320 1350 240 V0"
            stroke="#d9d9d9" stroke-width="3" stroke-dasharray="18 16"/>
    </g>
    <g class="arrows" fill="var(--green)">
      <polygon points="400,958 445,930 445,990"/>
      <polygon points="450,632 508,632 472,680"/>
      <polygon points="845,652 892,616 892,675"/>
      <polygon points="888,353 946,356 908,402"/>
      <polygon points="1300,385 1348,348 1348,408"/>
    </g>
    <g class="connectors" stroke="var(--road)" stroke-width="5">
      <line x1="400" y1="872" x2="430" y2="898"/>
      <line x1="525" y1="688" x2="548" y2="708"/>
      <line x1="828" y1="568" x2="856" y2="590"/>
      <line x1="948" y1="418" x2="972" y2="440"/>
      <line x1="1280" y1="303" x2="1308" y2="325"/>
    </g>
    <g class="badges" fill="url(#badge-fill)" stroke="var(--road)" stroke-width="5">
      <circle cx="350" cy="820" r="73"/>
      <circle cx="598" cy="755" r="73"/>
      <circle cx="770" cy="517" r="73"/>
      <circle cx="1022" cy="492" r="73"/>
      <circle cx="1225" cy="252" r="73"/>
    </g>
    <g class="icons" fill="#fff">
      <!-- person with phone -->
      <circle cx="348" cy="798" r="22"/>
      <path d="M316 856 C316 830 330 820 348 820 C366 820 380 830 380 856 Z"/>
      <circle cx="378" cy="843" r="21" stroke="var(--green-dark)" stroke-width="3"/>
      <path d="M370 835 l5 -3 4 6 -3 3 c2 4 4 6 7 7 l3 -3 6 4 -3 5 c-10 0 -19 -9 -19 -19z" fill="var(--green-dark)"/>
      <!-- location pin -->
      <path d="M598 712 C620 712 636 728 636 750 C636 772 616 790 598 802 C580 790 560 772 560 750 C560 728 576 712 598 712 Z"/>
      <circle cx="598" cy="746" r="14" fill="var(--green)"/>
      <!-- pencil and ruler -->
      <g transform="rotate(45 770 517)">
        <rect x="755" y="465" width="30" height="104" rx="3" fill="none" stroke="#fff" stroke-width="6"/>
        <path d="M785 480 h-10 M785 500 h-10 M785 520 h-14 M785 540 h-10 M785 556 h-10" stroke="#fff" stroke-width="4"/>
      </g>
      <g transform="rotate(-45 770 517)">
        <rect x="758" y="462" width="24" height="80" rx="2"/>
        <polygon points="758,545 782,545 770,572"/>
      </g>
      <!-- hard hat over gear -->
      <path d="M980 482 C980 452 998 438 1022 438 C1046 438 1064 452 1064 482 Z"/>
      <rect x="974" y="482" width="96" height="10" rx="3"/>
      <rect x="1012" y="432" width="20" height="16" rx="3" fill="var(--green)" stroke="#fff" stroke-width="4"/>
      <path d="M988 498 h68 a34 34 0 0 1 -68 0 Z"/>
      <path d="M984 505 l-10 4 4 14 10 -3 Z M1060 505 l10 4 -4 14 -10 -3 Z M1012 530 h20 v10 h-20 Z"/>
      <circle cx="1022" cy="506" r="12" fill="var(--green)"/>
      <!-- star -->
      <polygon points="1225,200 1240,232 1275,236 1249,260 1256,295 1225,278 1194,295 1201,260 1175,236 1210,232"/>
    </g>
  </svg>

  <header class="headline">
    <span class="headline-number">3</span>
    <h1 class="headline-text">Things<br>That Set<br>Us Apart</h1>
  </header>
  <ol class="advantages">
    <li>1. Lorem ipsum dolor sit amet,</li>
    <li>2. Lorem ipsum dolor sit amet,</li>
    <li>3. Lorem ipsum dolor sit amet,</li>
  </ol>

  <section class="step step--right step-call">
    <h2 class="step-title">INITIAL<br>CALL</h2>
    <p class="step-note">CAN WE HELP?</p>
  </section>
  <section class="step step-visit">
    <h2 class="step-title">SITE VISIT</h2>
    <p class="step-note">DISCUSS, PLAN, DREAM</p>
  </section>
  <section class="step step--right step-design">
    <h2 class="step-title">DESIGN<br>PROPOSED</h2>
  </section>
  <section class="step step-install">
    <h2 class="step-title">INSTALATION<br>CONSTRUCTION</h2>
  </section>
  <section class="step step--right step-complete">
    <h2 class="step-title">COMPLETE</h2>
    <p class="step-note">KICK BACK + RELAX<br>WITH A SMILE ON YOUR FACE</p>
  </section>

  <div class="brand">
    <span class="brand-dot"></span>
    <span class="brand-name">Brindle Fern Yards</span>
  </div>
  <p class="tagline">Creating Exceptional Outdoor Living Spaces</p>
</main>
</body>
</html>
```